Cool modern, tech Business card design

Looking for a new business card design for our Managed IT Services company. We would like 2 sides, with the logo one one side horizontally and then the information on the back in either vertical or horizontal. We want our colors from the logo incorporated but also would like to see the color gray in there as well.

Target Market(s)

IT, Information Technology, Tech, Service

Industry/Entity Type

It Service

Contact Information for Business Card

Carl Penner
Managing Partner
(P)555-271-4830 ext xxx
(F)555-271-4831
www.brixtelcore.com

Font styles to use
Sans Serif

Colors
959595
000000
ec1f27

Requirements
Must have
• Logo on one side with some nice design or pattern
• Information on back in either vertical or horizontal format
Nice to have
• For it to look cool, tech, modern, stand out.

```html
<!DOCTYPE html>
<html lang="en">
<head>
<meta charset="utf-8">
<title>Brixtelcore Business Card</title>
<link rel="stylesheet" href="https://fonts.googleapis.com/css2?family=Open+Sans:wght@400;600&display=swap">
<style>
  :root {
    --bg: #3a3430;
    --card: #0b0b0b;
    --red: #ec1f27;
    --gray: #959595;
    --silver: #d6d6d6;
    --text: #e6e6e6;
    --divider: #2a2a2a;
  }
  * { margin: 0; padding: 0; box-sizing: border-box; }
  html, body { width: 1200px; height: 844px; overflow: hidden; }
  body {
    background: var(--bg);
    font-family: "Open Sans", sans-serif;
    position: relative;
  }
  .card {
    position: absolute;
    top: 272px;
    width: 520px;
    height: 300px;
    background: var(--card);
    box-shadow: 0 10px 30px rgba(0,0,0,.5);
  }
  .card--info { left: 60px; }
  .card--brand { left: 620px; }

  .brand {
    position: absolute;
    display: flex;
    align-items: center;
    gap: 10px;
    font-weight: 600;
    letter-spacing: -0.5px;
    white-space: nowrap;
  }
  .brand__mark { width: 14px; height: 14px; flex: none; }
  .card--info .brand {
    left: 34px; top: 126px;
    font-size: 40px;
    color: var(--red);
  }
  .card--info .brand__mark { background: var(--red); }
  .card--brand .brand {
    left: 0; right: 0; top: 118px;
    justify-content: center;
    font-size: 50px;
    color: var(--silver);
  }
  .card--brand .brand__mark { background: var(--silver); }

  .divider {
    position: absolute;
    left: 300px; top: 40px;
    width: 1px; height: 220px;
    background: var(--divider);
  }
  .contact {
    position: absolute;
    left: 326px; top: 78px;
    color: var(--text);
    white-space: nowrap;
  }
  .contact__name {
    color: var(--red);
    font-size: 16px;
    font-weight: 600;
    text-transform: uppercase;
    line-height: 1.1;
  }
  .contact__title { font-size: 13px; margin-bottom: 22px; }
  .contact__list { list-style: none; }
  .contact__item {
    display: flex;
    align-items: center;
    gap: 7px;
    font-size: 13.5px;
    line-height: 1.55;
  }
  .contact__icon { width: 10px; height: 10px; fill: var(--red); flex: none; }
</style>
</head>
<body>
  <section class="card card--info">
    <div class="brand"><span class="brand__mark"></span>brixtelcore</div>
    <div class="divider"></div>
    <div class="contact">
      <p class="contact__name">Carl Penner</p>
      <p class="contact__title">Managing Director</p>
      <ul class="contact__list">
        <li class="contact__item">
          <svg class="contact__icon" viewBox="0 0 10 10" aria-hidden="true"><path d="M1 3c0-1 1-2 4-2s4 1 4 2v1H7V3H3v1H1zM2 5h6l1 4H1z"/></svg>
          555-271-4830 Ext: 318
        </li>
        <li class="contact__item">
          <svg class="contact__icon" viewBox="0 0 10 10" aria-hidden="true"><path d="M2 0h5v3H2zM0 4h10v5H0zM3 6h4v1H3z"/></svg>
          555-271-4831
        </li>
        <li class="contact__item">
          <svg class="contact__icon" viewBox="0 0 10 10" aria-hidden="true"><circle cx="5" cy="5" r="5"/></svg>
          www.brixtelcore.com
        </li>
      </ul>
    </div>
  </section>

  <section class="card card--brand">
    <div class="brand"><span class="brand__mark"></span>brixtelcore</div>
  </section>
</body>
</html>
```